Business Card - Business Consultancy

Newly Established Company, specializing in Business Consultancy, Human Resource Management, Talent Acquisition and Payroll Solutions.

We need a Business card design which portrays "elegance" and a very sleek yet business-like design. We would like a nice blue trimming (which goes well with the logo) to separate the content of the business card at the top. We would also like to see the design using the color silver either as a background or incorporated into it.

The final design should be a Business card which has colors matching the logo; a nice font; the above-mentioned specifics that adheres to the theme of "a stylish and professional business"

FYI: please do not have too fanciful designs.

Industry/Entity Type

Business Consultant

Contact Information for Business Card

Marcus Tellon
Business Development Director
Brightpath HR Consulting Private Limited
27 Wexford Lane, #05-03B
Harbourview Trade Tower
Singapore 061739
Mobile : (+65) 94386157
Email : mtellon@brightpathhr-advisory.com
Alternative : brightpathhradvisory@mailbox-example.com

Requirements
Must have
• Nice Blue Trimming matching Logo which separates content, see attached
• Design incorporates either a silver background or the use of the color silver
Should not have
• No Fanciful Designs
• No Childish Designs
• No Overly Complicated Designs

```html
<!DOCTYPE html>
<html lang="en">
<head>
<meta charset="utf-8">
<title>Brightpath HR Consulting – Business Card</title>
<link rel="stylesheet" href="https://fonts.googleapis.com/css2?family=Open+Sans:wght@400;600&display=swap">
<style>
  :root {
    --bg: #5a4a44;
    --card: #151515;
    --card-edge: #222222;
    --blue: #1f8fd6;
    --green: #7dc142;
    --text: #ececec;
    --silver: #c0c0c0;
    --silver-dim: #9a9a9a;
  }
  * { margin: 0; padding: 0; box-sizing: border-box; }
  html, body { width: 1200px; height: 814px; overflow: hidden; }
  body {
    background: var(--bg);
    font-family: "Open Sans", Arial, sans-serif;
    position: relative;
  }
  .card {
    position: absolute;
    width: 540px;
    height: 320px;
    background: var(--card);
    border: 1px solid var(--card-edge);
    border-radius: 4px;
    box-shadow: 0 10px 24px rgba(0,0,0,.35);
    color: var(--text);
    overflow: hidden;
  }
  .card--front { left: 40px; top: 247px; }
  .card--back  { left: 620px; top: 247px; }

  .brand {
    position: absolute;
    display: flex;
    align-items: center;
    gap: 10px;
  }
  .brand__dot {
    width: 34px; height: 34px;
    border-radius: 50%;
    background: var(--blue);
    flex: none;
  }
  .brand__name {
    font-weight: 600;
    color: var(--text);
    white-space: nowrap;
  }
  .card--front .brand { right: 40px; top: 30px; }
  .card--front .brand__name { font-size: 22px; }

  .rule { position: absolute; }
  .rule--top { left: 270px; right: 40px; top: 92px; height: 2px; background: var(--blue); }
  .rule--mid { left: 0; width: 270px; top: 176px; height: 1px; background: var(--silver); }

  .contact {
    position: absolute;
    right: 40px;
    top: 102px;
    text-align: right;
    font-size: 13px;
    line-height: 21px;
  }
  .contact__row { display: flex; justify-content: flex-end; align-items: center; gap: 8px; }
  .contact__icon { width: 12px; height: 12px; flex: none; }
  .contact__label { color: var(--silver); }

  .person {
    position: absolute;
    left: 26px;
    top: 182px;
  }
  .person__name { font-size: 18px; font-weight: 600; color: var(--blue); line-height: 24px; }
  .person__title { font-size: 14px; color: var(--green); line-height: 19px; }
  .person__address { margin-top: 4px; font-size: 14px; line-height: 18px; color: var(--silver); font-style: normal; }

  .card--back .brand {
    left: 0; right: 0; top: 96px;
    justify-content: center;
  }
  .card--back .brand__dot { width: 48px; height: 48px; }
  .card--back .brand__name { font-size: 26px; }
  .website {
    position: absolute;
    left: 0; right: 0; top: 200px;
    text-align: center;
    font-size: 13px;
    letter-spacing: .5px;
    color: var(--silver);
  }
</style>
</head>
<body>
  <section class="card card--front">
    <div class="brand">
      <span class="brand__dot"></span>
      <span class="brand__name">Brightpath HR</span>
    </div>
    <div class="rule rule--top"></div>

    <div class="contact">
      <div class="contact__row">
        <span>(+65) 94386157</span>
        <svg class="contact__icon" viewBox="0 0 12 12" aria-hidden="true">
          <rect x="2.5" y="0.5" width="7" height="11" rx="1.2" fill="none" stroke="var(--blue)" stroke-width="1.2"/>
          <rect x="5" y="9.3" width="2" height="1" fill="var(--blue)"/>
        </svg>
      </div>
      <div class="contact__row">
        <span>mtellon@brightpathhr-advisory.com</span>
        <svg class="contact__icon" viewBox="0 0 12 12" aria-hidden="true">
          <rect x="0.5" y="2" width="11" height="8" rx="1" fill="var(--blue)"/>
          <path d="M1 2.6 L6 6.6 L11 2.6" fill="none" stroke="var(--card)" stroke-width="1"/>
        </svg>
      </div>
      <div class="contact__row">
        <span><span class="contact__label">Alternative:</span> brightpathhradvisory@mailbox-example.com</span>
      </div>
    </div>

    <div class="rule rule--mid"></div>

    <div class="person">
      <div class="person__name">Marcus Tellon</div>
      <div class="person__title">Business Development Director</div>
      <address class="person__address">
        Brightpath HR Consulting Private Limited<br>
        27 Wexford Lane, #05-03B<br>
        Harbourview Trade Tower<br>
        Singapore 061739
      </address>
    </div>
  </section>

  <section class="card card--back">
    <div class="brand">
      <span class="brand__dot"></span>
      <span class="brand__name">Brightpath HR</span>
    </div>
    <div class="website">www.brightpathhr-advisory.com</div>
  </section>
</body>
</html>
```